Orchard Pulp Bottle Label

We need a new label design for our juice bottles. The name of our company is Orchard Pulp. We are looking for a modification rather than a complete redesign.
If you look at our website www.orchardpulp-example.com you will see the bottles/labels that we use. We are looking for the next generation of this label. A clean/modern look but something that looks more professional. We want to use the same colors and the same juice man logo other than that we are open to new concepts.
Our competitors are squeeze lane and greenvale juice. Our goal is to have a label that will stand up to their labels and look just as professional.
Thanks in advance.
Teo Marchetti

```html
<!DOCTYPE html>
<html lang="en">
<head>
<meta charset="utf-8">
<title>Orchard Pulp – G3 Bottle Label</title>
<link rel="stylesheet" href="https://fonts.googleapis.com/css2?family=Source+Sans+3:ital,wght@0,400;0,600;0,700;1,700;1,900&display=swap">
<style>
  :root {
    --backdrop: #e4e4e4;
    --label-green: #0b8c3b;
    --label-green-light: #3aa83a;
    --label-shadow-green: #066a2b;
    --text-white: #ffffff;
    --mark-orange: #f2a51c;
  }

  html, body {
    margin: 0;
    padding: 0;
    width: 1200px;
    height: 2882px;
    overflow: hidden;
    background: var(--backdrop);
  }

  .canvas {
    position: relative;
    width: 1200px;
    height: 2882px;
    font-family: "Source Sans 3", "Myriad Pro", Arial, sans-serif;
    color: var(--text-white);
  }

  .label {
    position: absolute;
    left: 80px;
    top: 462px;
    width: 1040px;
    height: 1958px;
    background: linear-gradient(90deg, var(--label-green) 0%, var(--label-green) 62%, var(--label-green-light) 100%);
  }

  .brand {
    position: absolute;
    left: 190px;
    top: 142px;
    display: flex;
    align-items: center;
    gap: 22px;
  }

  .brand-mark {
    width: 72px;
    height: 72px;
    border-radius: 50%;
    background: var(--mark-orange);
  }

  .brand-name {
    font-weight: 700;
    font-size: 72px;
    letter-spacing: -1px;
    line-height: 1;
  }

  .headline {
    position: absolute;
    left: 176px;
    top: 352px;
    margin: 0;
    font-weight: 700;
    font-size: 158px;
    line-height: 170px;
    letter-spacing: -2px;
  }

  .ingredients {
    position: absolute;
    right: 160px;
    top: 1080px;
    margin: 0;
    padding: 0;
    list-style: none;
    text-align: right;
    font-weight: 400;
    font-size: 84px;
    line-height: 119px;
  }

  .variant-code {
    position: absolute;
    left: 180px;
    top: 1480px;
    margin: 0;
    font-weight: 900;
    font-style: italic;
    font-size: 216px;
    line-height: 1;
    letter-spacing: -4px;
    text-shadow: 14px 10px 0 var(--label-shadow-green);
  }

  .volume {
    position: absolute;
    right: 160px;
    top: 1832px;
    margin: 0;
    font-weight: 400;
    font-size: 42px;
    line-height: 1;
  }
</style>
</head>
<body>
  <main class="canvas">
    <section class="label">
      <div class="brand">
        <span class="brand-mark"></span>
        <span class="brand-name">Orchard Pulp</span>
      </div>

      <h1 class="headline">100%<br>Natural<br>Fresh Juice</h1>

      <ul class="ingredients">
        <li>cilanto</li>
        <li>kale</li>
        <li>pinapple</li>
        <li>coconut</li>
        <li>lime</li>
      </ul>

      <p class="variant-code">G3</p>

      <p class="volume">16oz 473ml</p>
    </section>
  </main>
</body>
</html>
```